BOLT Banner Ads for businesses who are keeping up with NRB guidelines

Banner ads - banner ad templates for us to advertise. We need this to be available in all of the key sizes for pomvia adlines and VS. Keep in mind, I want the template so we can adjust the wording. Sample wording is below:
NRB Compliant; BOLT Certified
Worried about COVID 19? Visit BOLT Certified Businesses
Protect you and your family, go to BOLT Certified Businesses
We are BOLT Certified, come see us today!
BOLT Certified businesses; giving you confidence
Be Confident with a BOLT Certification

Please feel free to check out our other contests for a better sense of the look and feel:
https://jobs.crewmosaic.com/job/5162078
https://jobs.crewmosaic.com/job/5162391

Target Market(s)

These ads are aimed at the general public to announce the certification.

Requirements
Must have
• We need the different banner sizes for pomvia adlines, vexaspot marketing, etc.

```html
<!DOCTYPE html>
<html lang="en">
<head>
<meta charset="utf-8">
<title>BOLT Certified Banner Ads</title>
<link rel="stylesheet" href="https://fonts.googleapis.com/css2?family=Oswald:wght@600&family=Montserrat:wght@500;600&display=swap">
<style>
  :root {
    --stage: #232323;
    --sky-top: #f4f9fe;
    --sky-mid: #dbeefc;
    --sky-low: #b9dcf6;
    --navy: #0d4a94;
    --ink: #111a24;
    --brand-dot: #2f7fc4;
    --button: #3f8d3a;
    --button-edge: #2f6f2b;
    --white: #ffffff;
  }
  * { margin: 0; padding: 0; box-sizing: border-box; }
  html, body { width: 1200px; height: 900px; overflow: hidden; background: var(--stage); }
  .stage { position: relative; width: 1200px; height: 900px; }

  .banner {
    position: absolute;
    overflow: hidden;
    background:
      radial-gradient(ellipse at 70% 85%, var(--sky-low) 0%, rgba(185,220,246,0) 60%),
      linear-gradient(180deg, var(--sky-top) 0%, var(--sky-mid) 55%, var(--sky-low) 100%);
    text-align: center;
  }
  .banner--square { left: 152px; top: 264px; width: 382px; height: 382px; }
  .banner--tall { left: 599px; top: 73px; width: 382px; height: 762px; }

  .brand {
    position: absolute; left: 0; right: 0;
    display: flex; align-items: center; justify-content: center; gap: 10px;
  }
  .brand__dot { border-radius: 50%; background: var(--brand-dot); }
  .brand__name {
    font-family: "Montserrat", sans-serif; font-weight: 500;
    color: var(--ink); letter-spacing: 1px;
  }
  .banner--square .brand { top: 48px; }
  .banner--square .brand__dot { width: 40px; height: 40px; }
  .banner--square .brand__name { font-size: 38px; }
  .banner--tall .brand { top: 58px; }
  .banner--tall .brand__dot { width: 56px; height: 56px; }
  .banner--tall .brand__name { font-size: 50px; }

  .headline {
    position: absolute; left: 0; right: 0;
    font-family: "Oswald", sans-serif; font-weight: 600;
    color: var(--navy); text-transform: uppercase;
    font-size: 50px; line-height: 51px; letter-spacing: 0.3px;
    white-space: nowrap;
  }
  .headline__text {
    display: inline-block;
    transform: scaleX(0.81);
    transform-origin: center;
  }
  .banner--square .headline { top: 135px; }
  .banner--tall .headline { top: 167px; }

  .subline {
    position: absolute; left: 0; right: 0;
    font-family: "Montserrat", sans-serif; font-weight: 500;
    color: var(--ink); font-size: 19px; line-height: 1.35;
  }
  .banner--square .subline { top: 253px; }
  .banner--tall .subline { top: 285px; }

  .cta {
    position: absolute; left: 50%; transform: translateX(-50%);
    display: inline-flex; align-items: center; justify-content: center; gap: 6px;
    background: var(--button); color: var(--white);
    border-bottom: 2px solid var(--button-edge); border-radius: 3px;
    font-family: "Montserrat", sans-serif; font-weight: 600;
    text-transform: uppercase; white-space: nowrap; text-decoration: none;
  }
  .banner--square .cta { top: 326px; width: 124px; height: 26px; font-size: 15px; }
  .banner--tall .cta { top: 706px; width: 165px; height: 34px; font-size: 20px; }
  .cta svg { display: block; }

  .family-photo {
    position: absolute; left: 45px; top: 360px; width: 292px; height: 337px;
    clip-path: polygon(50% 0, 100% 22%, 100% 78%, 50% 100%, 0 78%, 0 22%);
    background: linear-gradient(160deg, #f2ece4 0%, #e4cfae 35%, #d9a25a 60%, #c9d5e4 100%);
  }
</style>
</head>
<body>
<main class="stage">

  <section class="banner banner--square" aria-label="Square banner ad">
    <div class="brand">
      <span class="brand__dot"></span>
      <span class="brand__name">BOLT</span>
    </div>
    <h1 class="headline"><span class="headline__text">Protect you and<br>your family</span></h1>
    <p class="subline">Go to BOLT<br>Certified Businesses</p>
    <a class="cta" href="#">View more
      <svg width="9" height="12" viewBox="0 0 9 12"><path d="M0 0 L9 6 L0 12 Z" fill="#fff"/></svg>
    </a>
  </section>

  <section class="banner banner--tall" aria-label="Tall banner ad">
    <div class="brand">
      <span class="brand__dot"></span>
      <span class="brand__name">BOLT</span>
    </div>
    <h1 class="headline"><span class="headline__text">Protect you and<br>your family</span></h1>
    <p class="subline">Go to BOLT<br>Certified Businesses</p>
    <div class="family-photo" role="img" aria-label="Photo of a mother and daughter wearing face masks, sharing fruit at home"></div>
    <a class="cta" href="#">View more
      <svg width="11" height="15" viewBox="0 0 11 15"><path d="M0 0 L11 7.5 L0 15 Z" fill="#fff"/></svg>
    </a>
  </section>

</main>
</body>
</html>
```